Four in One (Flexible infographic for Content Management Industry)

See attachment.
A graphic depicting 4 products, where each can stand on its own and each can be combined with others, but where, if all are taken together, the best result is achieved (the "super product").
Intended use is web. See attached file as an example.
The most basic idea is as the attached diagram shows, where 4 rectangles are arranged in a quadrangle, with a middle rectangle in the center representing the combined 4 products. This concept is fine except it is a bit too obvious as it stands. We are looking for either a variation of this or another concept.
The audience is technical + professional + enterprise - NOT consumers. Hence the design should be conservative in nature.
We are aware of tools like as Canva or Pictogram where such graphics are available, but we are looking for something with a bit more imagination and flexibility.
This graphic should be targeted to web sites and be delivered with vector-based (SVG) graphics.

```html
<!DOCTYPE html>
<html lang="en">
<head>
<meta charset="utf-8">
<title>Super Product – Four in One</title>
<link rel="stylesheet" href="https://fonts.googleapis.com/css2?family=Barlow+Condensed:wght@600;700&family=Lexend:wght@300;400&display=swap">
<style>
  :root {
    --page: #fdfdfd;
    --card: #f1f1f1;
    --ink: #2b2b2b;
    --purple: #7e71b0;
    --green: #8cc443;
    --teal: #00a59b;
    --blue: #1a7dba;
    --orange: #ef7f1c;
    --ring: #c6c7c6;
    --btn-grey: #9a9a9a;
  }
  * { box-sizing: border-box; margin: 0; padding: 0; }
  html, body { width: 1200px; height: 943px; overflow: hidden; background: var(--page); }
  .canvas { position: relative; width: 1200px; height: 943px; }

  .card {
    position: absolute; width: 459px; height: 347px;
    background: var(--card); border-radius: 50px; overflow: hidden;
  }
  .card--tl { left: 108px; top: 90px; }
  .card--tr { left: 641px; top: 90px; }
  .card--bl { left: 108px; top: 512px; }
  .card--br { left: 641px; top: 512px; }

  .badge {
    position: absolute; width: 164px; height: 164px; border-radius: 50%;
    display: flex; align-items: center; justify-content: center;
  }
  .card--tl .badge { left: -50px; top: -55px; background: var(--purple); }
  .card--tr .badge { right: -51px; top: -55px; background: var(--green); }
  .card--bl .badge { left: -50px; top: -55px; background: var(--teal); }
  .card--br .badge { right: -51px; top: -55px; background: var(--blue); }
  .badge svg { width: 54px; height: 54px; }
  .card--tl .badge svg, .card--bl .badge svg { transform: translate(4px, 8px); }
  .card--tr .badge svg, .card--br .badge svg { transform: translate(-6px, 8px); }

  .card__title {
    position: absolute; font-family: "Barlow Condensed", sans-serif; font-weight: 600;
    font-size: 22px; line-height: 27px;
  }
  .card--tl .card__title { left: 138px; top: 46px; color: var(--purple); }
  .card--tr .card__title { right: 138px; top: 46px; color: var(--green); }
  .card--bl .card__title { left: 138px; top: 66px; color: var(--teal); }
  .card--br .card__title { right: 138px; top: 64px; color: var(--blue); }

  .card__body {
    position: absolute; font-family: "Lexend", sans-serif; font-weight: 300;
    font-size: 12.3px; line-height: 17.4px; color: var(--ink); width: 300px;
  }
  .card--tl .card__body { left: 111px; top: 111px; }
  .card--tr .card__body { left: 135px; top: 111px; }
  .card--bl .card__body { left: 111px; top: 147px; width: 320px; }
  .card--br .card__body { left: 135px; top: 137px; }
  .features { list-style: none; }
  .features li::before { content: "\2714"; font-size: 9px; margin-right: 4px; vertical-align: 1px; }

  .button {
    position: absolute; width: 110px; height: 26px; border-radius: 13px; overflow: hidden;
    display: flex; font-family: "Lexend", sans-serif; font-size: 10.5px; color: #fff;
  }
  .card--tl .button, .card--bl .button { left: 43px; }
  .card--tr .button, .card--br .button { left: 305px; }
  .card--tl .button, .card--tr .button { top: 283px; }
  .card--bl .button, .card--br .button { top: 290px; }
  .button__label { flex: 1; display: flex; align-items: center; justify-content: center; }
  .button__arrow { width: 25px; background: var(--btn-grey); display: flex; align-items: center; justify-content: center; }
  .card--tl .button__label { background: var(--purple); }
  .card--tr .button__label { background: var(--green); }
  .card--bl .button__label { background: var(--teal); }
  .card--br .button__label { background: var(--blue); }

  .hub { position: absolute; left: 439px; top: 311px; width: 328px; height: 328px; border-radius: 50%; background: var(--page); }
  .hub__ring { position: absolute; left: 451px; top: 323px; width: 304px; height: 304px; border-radius: 50%; background: var(--ring); }
  .hub__core {
    position: absolute; left: 478px; top: 350px; width: 250px; height: 250px; border-radius: 50%;
    background: var(--orange); color: #fff; display: flex; flex-direction: column;
    align-items: center; justify-content: center;
    font-family: "Barlow Condensed", sans-serif; font-weight: 700; font-size: 58px; line-height: 64px;
  }
</style>
</head>
<body>
<main class="canvas">

  <section class="card card--tl">
    <div class="badge">
      <svg viewBox="0 0 54 54" fill="none" stroke="#fff" stroke-width="2">
        <rect x="14" y="4" width="30" height="40"/><rect x="10" y="8" width="30" height="40"/><rect x="6" y="12" width="30" height="40" fill="var(--purple)"/>
        <path d="M10 18h22M10 22h22M10 26h22M10 30h22M10 34h22M10 38h22M10 42h22M10 46h22"/>
      </svg>
    </div>
    <h2 class="card__title">Document Management</h2>
    <div class="card__body">
      <p>Streamline document organization, access, and collaboration with easier file storage and sharing, leading to more efficient workflows.</p>
      <ul class="features">
        <li>Centralize Document Center</li>
        <li>Collaborative Workspace Integration</li>
        <li>Automated Compliance &nbsp;&nbsp;&nbsp;Tracking</li>
        <li>Check 4</li>
      </ul>
    </div>
    <a class="button"><span class="button__label">Learn More</span><span class="button__arrow"><svg width="8" height="9"><path d="M0 0L8 4.5L0 9Z" fill="#fff"/></svg></span></a>
  </section>

  <section class="card card--tr">
    <div class="badge">
      <svg viewBox="0 0 54 54" fill="none" stroke="#fff" stroke-width="2">
        <path d="M27 3L8 10v14c0 12 8 20 19 25c11-5 19-13 19-25V10Z"/>
        <path d="M27 8L13 13v11c0 9 6 16 14 20c8-4 14-11 14-20V13Z"/>
        <rect x="20" y="24" width="14" height="11" rx="2"/><path d="M22 24v-4a5 5 0 0 1 10 0v4M27 28v3"/>
        <path d="M2 51h50"/>
      </svg>
    </div>
    <h2 class="card__title">Security and Compliance</h2>
    <div class="card__body">
      <p>Benefit from tailored cloud solutions, secure data storage, and expert disaster recovery planning for reliable and scalable IT operations.</p>
      <ul class="features">
        <li>Custom Cloud Solutions</li>
        <li>Secure Data Storage</li>
        <li>Expert Disaster Recovery</li>
        <li>Check 4</li>
      </ul>
    </div>
    <a class="button"><span class="button__label">Learn More</span><span class="button__arrow"><svg width="8" height="9"><path d="M0 0L8 4.5L0 9Z" fill="#fff"/></svg></span></a>
  </section>

  <section class="card card--bl">
    <div class="badge">
      <svg viewBox="0 0 54 54" fill="none" stroke="#fff" stroke-width="2">
        <circle cx="16" cy="36" r="6"/><circle cx="16" cy="36" r="11" stroke-dasharray="4 3"/>
        <circle cx="38" cy="16" r="5"/><circle cx="38" cy="16" r="10" stroke-dasharray="4 3"/>
        <circle cx="20" cy="8" r="3"/><circle cx="6" cy="18" r="2"/>
        <path d="M41 31h8M41 35h8M41 39h8M41 43h8M41 47h8"/>
      </svg>
    </div>
    <h2 class="card__title">Enterprise Resource<br>Planning</h2>
    <div class="card__body">
      <p>Simplify management<br>across finance, sales, and operations, enabling better decision-making and improved productivity.</p>
      <ul class="features">
        <li>Integrated Business Processes</li>
        <li>Enhanced Decision-Making</li>
        <li>Productivity Improvement</li>
        <li>Check 4</li>
      </ul>
    </div>
    <a class="button"><span class="button__label">Learn More</span><span class="button__arrow"><svg width="8" height="9"><path d="M0 0L8 4.5L0 9Z" fill="#fff"/></svg></span></a>
  </section>

  <section class="card card--br">
    <div class="badge">
      <svg viewBox="0 0 54 54" fill="none" stroke="#fff" stroke-width="2">
        <circle cx="27" cy="25" r="20" stroke-dasharray="6 3"/>
        <circle cx="27" cy="25" r="13"/><ellipse cx="27" cy="25" rx="6" ry="13"/>
        <path d="M14 25h26M16 18h22M16 32h22M27 12v26M27 45v5M6 51h42"/>
      </svg>
    </div>
    <h2 class="card__title">Digital Transformation</h2>
    <div class="card__body">
      <p>Turn scanned document &nbsp;into easily searchable digital &nbsp;archives, boosting efficiency and accessibility.</p>
      <ul class="features">
        <li>Instant searchable Archives with OCR</li>
        <li>Automated Document Classification</li>
        <li>TeamVault and Cloud Blob Ready</li>
        <li>Check 4</li>
      </ul>
    </div>
    <a class="button"><span class="button__label">Learn More</span><span class="button__arrow"><svg width="8" height="9"><path d="M0 0L8 4.5L0 9Z" fill="#fff"/></svg></span></a>
  </section>

  <div class="hub"></div>
  <div class="hub__ring"></div>
  <div class="hub__core"><span>SUPER</span><span>PRODUCT</span></div>

</main>
</body>
</html>
```